Business Card and Simple Logo Desgin

New Zealand based start up company "Brook Advisory LTD" requires business cards and simple logo design.

Card Content.

Brook Advisory LTD

Joanna Pritchard
CA, BMS (Hons)

j.pritchard@brookadvisory.co.nz
PH +64 21 574 160

Target Market(s)

Corporate Business in IT, Finance and accounting.

Industry/Entity Type

Business

```html
<!DOCTYPE html>
<html lang="en">
<head>
<meta charset="utf-8">
<title>Brook Advisory – Business Card</title>
<link rel="stylesheet" href="https://fonts.googleapis.com/css2?family=Fira+Sans:wght@400;600&family=Gelasio:wght@400;700&display=swap">
<style>
  :root {
    --bg: #1b1b1d;
    --card-white: #ffffff;
    --brand-blue: #1f62b8;
    --brand-orange: #f5a511;
    --ink: #3b3b3b;
    --ink-soft: #555555;
    --back-top: #1349ad;
    --back-bottom: #0a2f7e;
  }
  * { margin: 0; padding: 0; box-sizing: border-box; }
  html, body {
    width: 1200px;
    height: 900px;
    overflow: hidden;
    background: var(--bg);
  }
  .stage {
    position: relative;
    width: 1200px;
    height: 900px;
  }
  .card {
    position: absolute;
    left: 320px;
    width: 560px;
    height: 320px;
    border-radius: 24px;
  }
  .card--front {
    top: 90px;
    background: var(--card-white);
  }
  .card--back {
    top: 490px;
    background: linear-gradient(180deg, var(--back-top), var(--back-bottom));
  }
  .brand {
    position: absolute;
    left: 0;
    right: 0;
    display: flex;
    align-items: center;
    justify-content: center;
    gap: 12px;
  }
  .brand__dot {
    width: 30px;
    height: 30px;
    border-radius: 50%;
    background: var(--brand-orange);
  }
  .brand__name {
    font-family: "Gelasio", Georgia, serif;
    font-weight: 400;
    font-size: 42px;
    line-height: 1;
  }
  .card--front .brand { top: 62px; }
  .card--front .brand__name { color: var(--brand-blue); }
  .card--back .brand { top: 110px; }
  .card--back .brand__name { color: var(--brand-orange); }
  .person {
    position: absolute;
    top: 150px;
    left: 0;
    right: 0;
    text-align: center;
    font-family: "Fira Sans", Arial, sans-serif;
  }
  .person__name {
    font-weight: 600;
    font-size: 26px;
    color: var(--ink);
  }
  .person__credentials {
    margin-top: 2px;
    font-size: 16px;
    color: var(--ink-soft);
  }
  .contacts {
    position: absolute;
    top: 238px;
    left: 0;
    right: 0;
    list-style: none;
    font-family: "Fira Sans", Arial, sans-serif;
    font-size: 17px;
    color: var(--ink);
    text-align: center;
  }
  .contacts li {
    display: flex;
    align-items: center;
    justify-content: center;
    gap: 7px;
    line-height: 24px;
  }
  .contacts__tag {
    display: inline-flex;
    align-items: center;
    justify-content: center;
    width: 17px;
    height: 17px;
    background: var(--brand-orange);
    color: #ffffff;
    font-size: 13px;
  }
  .website {
    position: absolute;
    top: 172px;
    left: 0;
    right: 0;
    text-align: center;
    font-family: "Gelasio", Georgia, serif;
    font-weight: 700;
    font-size: 15px;
    color: #ffffff;
  }
</style>
</head>
<body>
<main class="stage">
  <section class="card card--front" aria-label="Business card front">
    <div class="brand">
      <span class="brand__dot"></span>
      <span class="brand__name">Brook Advisory</span>
    </div>
    <div class="person">
      <p class="person__name">Joanna Pritchard</p>
      <p class="person__credentials">CA, BMS (Hons)</p>
    </div>
    <ul class="contacts">
      <li><span class="contacts__tag">e</span>j.pritchard@brookadvisory.co.nz</li>
      <li><span class="contacts__tag">m</span>+64 21 574 160</li>
    </ul>
  </section>

  <section class="card card--back" aria-label="Business card back">
    <div class="brand">
      <span class="brand__dot"></span>
      <span class="brand__name">Brook Advisory</span>
    </div>
    <p class="website">www.brookadvisory.co.nz</p>
  </section>
</main>
</body>
</html>
```